CD-/Plattencover für eine Tonträgerfirma
Zielgruppe
Wir sind eine Tonträgerfirma und bewegen uns im Low-Budget-Segment.
Aufgabenstellung
'Harbor Lanterns'
Wir benötigen nicht das komplette Artwork, sondern ein Frontcover
(121 x 120 mm + 20 mm Beschnitt) wg. etwaiger Verschiebung der Positionierung.
Fertigstellung (Aufziehen des Inlays und Labels) erfolgt später bei uns im Hause.
Wir benötigen später eine offene psd-Datei mit allen Ebenen.
Wichtig: Schriften nicht gerastert ggfs. Schrift mitliefern.
Was wir uns vorstellen:
- Entsprechend der Musik Bild
- Da es ein 2-CD-Set ist, sollte '2 CDs' auch gut auf dem Cover ersichtlich sein
- Folgende Titel sollten auf dem Cover genannt werden
Rowan Lad
Hills of Fern
Gentle Harrow
- Bildmaterial sollte bei pixelbarn, bildora oder n-pics ausgesucht werden,
das Bildmaterial wird dann später auch von uns dort eingekauft
- keine Künstlerfotos
- vorzugsweise nur 1 Bild pro Layout, max. 2 Bilder
Wir freuen uns und sind sehr gespannt auf eure Vorschläge,
bei Fragen gerne mailen

```html
<!DOCTYPE html>
<html lang="en">
<head>
<meta charset="utf-8">
<title>Harbor Lanterns – Front Cover</title>
<link href="https://fonts.googleapis.com/css2?family=Uncial+Antiqua&display=swap" rel="stylesheet">
<style>
  :root {
    --stage: #2b2b2b;
    --sky-top: #8f9a93;
    --sky-mid: #6f8a6a;
    --hill-gold: #b89a3a;
    --hill-green: #6c7a2a;
    --hill-dark: #4a3a1c;
    --cloak-dark: #3a2618;
    --cloak-red: #9a2a1c;
    --wood-light: #c99a68;
    --wood-mid: #a8764a;
    --wood-dark: #7d5432;
    --celtic-green: #3fc53a;
    --celtic-green-dark: #1f7a1c;
    --badge-green: #2faa2a;
    --track-white: #f4f1e8;
  }
  * { margin: 0; padding: 0; box-sizing: border-box; }
  html, body {
    width: 1200px; height: 829px; overflow: hidden;
    background: var(--stage);
  }
  .cover {
    position: absolute; left: 220px; top: 35px;
    width: 760px; height: 760px; overflow: hidden;
    font-family: "Uncial Antiqua", serif;
  }
  .cover__scene {
    position: absolute; inset: 0;
    background:
      radial-gradient(ellipse at 45% 80%, var(--hill-gold) 0%, var(--hill-green) 40%, transparent 70%),
      linear-gradient(180deg, var(--sky-top) 0%, var(--sky-mid) 32%, var(--hill-green) 58%, var(--hill-dark) 100%);
  }
  .cover__figure {
    position: absolute; right: 0; top: 60px;
    width: 230px; height: 640px;
    border-radius: 110px 40px 0 60px;
    background: linear-gradient(180deg, #c7a070 0%, var(--cloak-dark) 22%, var(--cloak-dark) 55%, var(--cloak-red) 80%, #6a1c12 100%);
  }
  .corner-mark {
    position: absolute; width: 42px; height: 42px;
    background: linear-gradient(135deg, var(--celtic-green), var(--celtic-green-dark));
  }
  .corner-mark--tl { left: 10px; top: 130px; }
  .corner-mark--tr { right: 30px; top: 10px; }
  .corner-mark--br { right: 10px; bottom: 140px; }
  .corner-mark--bl { left: 90px; bottom: 10px; }
  .title-sign {
    position: absolute; left: 60px; top: 240px;
    width: 420px; height: 210px;
    border-radius: 14px;
    transform: rotate(-8deg);
    background: repeating-linear-gradient(172deg, var(--wood-light) 0 9px, var(--wood-mid) 9px 13px, var(--wood-light) 13px 22px);
    box-shadow: inset 0 0 0 4px var(--wood-dark), 0 6px 14px rgba(0,0,0,.35);
    display: flex; flex-direction: column; justify-content: center; align-items: center;
  }
  .title-sign__main, .title-sign__sub {
    color: var(--celtic-green);
    text-shadow: 0 2px 0 var(--celtic-green-dark), 0 3px 4px rgba(0,0,0,.4);
    line-height: 1;
  }
  .title-sign__main { font-size: 62px; }
  .title-sign__sub { font-size: 50px; letter-spacing: 3px; margin-top: 8px; }
  .disc-badge {
    position: absolute; left: 410px; top: 195px;
    width: 70px; height: 70px; border-radius: 50%;
    background: var(--badge-green);
    box-shadow: 0 2px 5px rgba(0,0,0,.4);
    display: flex; align-items: center; justify-content: center;
    color: #111; font-size: 15px; font-weight: bold;
    font-family: Georgia, serif;
  }
  .track-list {
    position: absolute; left: 80px; top: 520px;
    list-style: none; transform: rotate(-8deg);
    color: var(--track-white); font-size: 26px;
    text-shadow: 0 2px 3px rgba(0,0,0,.6);
  }
  .track-list li { margin-bottom: 10px; }
  .track-list li:nth-child(2) { padding-left: 30px; }
  .track-list li:nth-child(3) { padding-left: 55px; }
</style>
</head>
<body>
  <main class="cover">
    <div class="cover__scene" role="img" aria-label="Photograph of green and golden highland hills under a cloudy sky with a faint large knotwork pattern"></div>
    <div class="cover__figure" role="img" aria-label="Photograph of a woman in a dark cloak and red dress seen from behind, looking over the hills"></div>

    <div class="corner-mark corner-mark--tl" role="img" aria-label="Green knotwork corner ornament"></div>
    <div class="corner-mark corner-mark--tr" role="img" aria-label="Green knotwork corner ornament"></div>
    <div class="corner-mark corner-mark--br" role="img" aria-label="Green knotwork corner ornament"></div>
    <div class="corner-mark corner-mark--bl" role="img" aria-label="Green knotwork corner ornament"></div>

    <div class="title-sign">
      <h1 class="title-sign__main">Harbor</h1>
      <span class="title-sign__sub">LANTERNS</span>
    </div>
    <div class="disc-badge">2 CDs</div>

    <ul class="track-list">
      <li>Rowan Lad</li>
      <li>Gentle Harrow</li>
      <li>Hills of Fern</li>
    </ul>
  </main>
</body>
</html>
```